Luxury Home Builder looking for an Exciting Homes Portfolio

We have a number of custom homes that we have completed over the years, and we want to give prospective clients are colorful and exciting catalog of our previous homes. I will provide access to the dropbox with all the photos. Need to get as many photos of homes in the catalog as possible. Please use verndalecustomdwell.com for pictures, lots of them in the portfolio, projects in progress, spec homes are available. I will provide full files to the winner. Need a very hip catalog to give out at events, and marketing venues.

Target Market(s)

High Net Worth Individuals looking for luxury homes

Industry/Entity Type

Real Estate Development

Requirements
Must have
• Photos of our project, please use verndalecustomdwell.com to get the photos, and will provide access to full pictures on dropbox to the winner.
• Logo must be incorporated.
Nice to have
• Clarification, website is not for design, but for the purposes of getting the photos. this has to be a very cool portfolio.

```html
<!DOCTYPE html>
<html lang="en">
<head>
<meta charset="utf-8">
<title>Verndale Crest Development — Portfolio</title>
<link href="https://fonts.googleapis.com/css2?family=Roboto:wght@300;400;500;700&display=swap" rel="stylesheet">
<style>
  :root{
    --backdrop:#efedeb;
    --paper:#ffffff;
    --paper-soft:#f1f1f1;
    --ink:#1d1d1f;
    --ink-muted:#6b6b6e;
    --bar:#111111;
    --sky-top:#5e58b3;
    --sky-mid:#b88fd2;
    --stone:#d9d2c8;
    --shadow-dark:#2c2824;
    --ghost:#dedede;
  }
  *{box-sizing:border-box;margin:0;padding:0}
  html,body{width:752px;height:1200px;overflow:hidden}
  body{background:var(--backdrop);font-family:"Roboto",Arial,sans-serif;color:var(--ink);position:relative}

  .page{position:absolute;background:var(--paper);box-shadow:0 2px 8px rgba(0,0,0,.12);overflow:hidden}

  .photo{position:absolute;background:linear-gradient(180deg,var(--sky-top) 0%,var(--sky-mid) 32%,var(--stone) 55%,#8d8378 72%,var(--shadow-dark) 100%)}
  .ghost-photo{position:absolute;background:linear-gradient(180deg,#f6f6f6 0%,var(--ghost) 55%,#cfcfcf 100%);opacity:.8}

  /* Front cover */
  .cover{left:40px;top:28px;width:432px;height:240px}
  .cover .photo{left:0;top:0;width:100%;height:150px}
  .cover-title{position:absolute;right:0;top:120px;width:250px;height:100px;background:var(--paper);padding:14px 18px}
  .cover-title .company{font-weight:300;font-size:21px;line-height:1.05;text-transform:uppercase;letter-spacing:.3px}
  .cover-title .company small{font-size:10px;text-transform:none}
  .cover-title .tagline{font-weight:700;font-size:13px;margin-top:8px}

  /* Back cover */
  .back{left:280px;top:290px;width:432px;height:240px;background:var(--paper-soft)}
  .back .ghost-photo{left:0;top:0;width:100%;height:100%}
  .brand{position:absolute;right:18px;top:18px;display:flex;align-items:center;gap:6px;font-size:9px;font-weight:500;letter-spacing:1.5px;color:var(--ink)}
  .brand .dot{width:10px;height:10px;border-radius:50%;background:var(--ink)}
  .back .photo{left:60px;top:56px;width:372px;height:100px}
  .contacts{position:absolute;left:60px;top:168px;display:flex;gap:34px;font-size:6.5px;line-height:1.5;color:var(--ink-muted)}

  /* Interior spread */
  .spread{left:40px;width:672px;height:300px;background:var(--paper-soft)}
  .spread-a{top:560px}
  .spread-b{top:884px}
  .spread .ghost-photo{left:0;top:0;width:336px;height:100%}
  .gutter{position:absolute;left:335px;top:0;width:2px;height:100%;background:linear-gradient(90deg,rgba(0,0,0,.08),rgba(0,0,0,0))}
  .spread .photo{left:208px;top:24px;width:464px;height:134px}
  .bar{display:block;background:var(--bar)}
  .project-intro{position:absolute;left:24px;top:128px}
  .project-intro .bar{width:64px;height:8px;margin-bottom:8px}
  .project-title{font-weight:300;font-size:21px;line-height:1.05;text-transform:uppercase}
  .project-facts{margin-top:10px;font-size:6.5px;line-height:1.55;color:var(--ink-muted)}
  .project-facts b{color:var(--ink);font-weight:500}
  .project-story{position:absolute;left:356px;top:172px;width:296px}
  .project-story .head{display:flex;align-items:center;gap:6px;font-size:8px;font-weight:500;text-transform:uppercase}
  .project-story .bar{width:40px;height:6px}
  .story-cols{display:flex;gap:14px;margin-top:8px;font-size:6.5px;line-height:1.55;color:var(--ink-muted)}
  .story-cols p{flex:1}
</style>
</head>
<body>

<section class="page cover">
  <div class="photo" role="img" aria-label="Mediterranean custom home at dusk with purple sky, arched facade and cypress trees"></div>
  <div class="cover-title">
    <div class="company">Verndale Crest<br>Development, <small>Inc.</small></div>
    <div class="tagline">Custom Luxury Homes</div>
  </div>
</section>

<section class="page back">
  <div class="ghost-photo" role="img" aria-label="Faded backdrop of the villa facade"></div>
  <div class="brand"><span class="dot"></span>VERNDALE</div>
  <div class="photo" role="img" aria-label="Wide dusk view of the Mediterranean villa and gardens"></div>
  <div class="contacts">
    <div>(555) 014-2280<br>Irvine, CA 92618</div>
    <div>T 555 014 2280<br>F 555 014 2281</div>
    <div>info@verndalecustomdwell.com<br>verndalecustomdwell.com</div>
  </div>
</section>

<section class="page spread spread-a">
  <div class="ghost-photo" role="img" aria-label="Faded backdrop of the villa entrance"></div>
  <div class="gutter"></div>
  <div class="photo" role="img" aria-label="Mediterranean custom home at dusk with lit windows and stone gate pillar"></div>
  <div class="project-intro">
    <span class="bar"></span>
    <h2 class="project-title">Mediterranean<br>Custom Home</h2>
    <div class="project-facts">
      <b>Project Size:</b> Estate<br>
      <b>Builder:</b> Verndale Crest<br>
      <b>Location:</b> Hillside Drive<br>
      <b>Sq. Ft.:</b> 8,400
    </div>
  </div>
  <div class="project-story">
    <div class="head"><span class="bar"></span>Mediterranean Custom Home</div>
    <div class="story-cols">
      <p>Set above the valley, this villa pairs hand-troweled plaster, arched loggias and a clay tile roof with a grand motor court. Every room opens toward the gardens and evening views.</p>
      <p>Interiors feature vaulted ceilings, stone floors and a chef's kitchen. A resort pool, outdoor lounge and guest casita complete a home built for gathering and quiet living.</p>
    </div>
  </div>
</section>

<section class="page spread spread-b">
  <div class="ghost-photo" role="img" aria-label="Faded backdrop of the villa entrance"></div>
  <div class="gutter"></div>
  <div class="photo" role="img" aria-label="Mediterranean custom home at dusk with lit windows and stone gate pillar"></div>
  <div class="project-intro">
    <span class="bar"></span>
    <h2 class="project-title">Mediterranean<br>Custom Home</h2>
    <div class="project-facts">
      <b>Project Size:</b> Estate<br>
      <b>Builder:</b> Verndale Crest<br>
      <b>Location:</b> Hillside Drive<br>
      <b>Sq. Ft.:</b> 8,400
    </div>
  </div>
  <div class="project-story">
    <div class="head"><span class="bar"></span>Mediterranean Custom Home</div>
    <div class="story-cols">
      <p>Set above the valley, this villa pairs hand-troweled plaster, arched loggias and a clay tile roof with a grand motor court. Every room opens toward the gardens and evening views.</p>
      <p>Interiors feature vaulted ceilings, stone floors and a chef's kitchen. A resort pool, outdoor lounge and guest casita complete a home built for gathering and quiet living.</p>
    </div>
  </div>
</section>

</body>
</html>
```